Website - Tides Of Bloom

We are catalysts of change in people's lives.
We work with individuals and professionals to bring about instant substantial & transforming change in their lives.
We provide one-on-one lifestyle coaching by an experienced practitioner.
Our existing website is www.tidesofbloom.biz & this site contains our the basis for the content of our desired new project, so please examine this carefully.
We require a professional and captivating website that will instantly impress, engage invite our readers to click & invest their lives.
Our services do not come cheap, but are second to none.
Our website must be contemporary whilst reflecting indisputable class & ultra-confidence in the success of our work.
Target Market(s)
Those who seek to want to change in their lives. Those aged primarily between 30 and 50 years of age, male or female.
Industry/Entity Type
Work
Look and feel

```html
<!DOCTYPE html>
<html lang="en">
<head>
<meta charset="utf-8">
<title>Tides Of Bloom</title>
<link href="https://fonts.googleapis.com/css2?family=Carlito:wght@400;700&display=swap" rel="stylesheet">
<style>
:root{
  --bg:#000;
  --text:#fff;
  --muted:#cfcfcf;
  --teal:#1a7fa0;
  --orange:#e0631f;
  --band:#3a3a3a;
  --search:#2e2e2e;
  --badge:#777;
}
*{margin:0;padding:0;box-sizing:border-box}
html,body{width:1011px;height:1200px;overflow:hidden;background:var(--bg)}
body{font-family:"Carlito",sans-serif;color:var(--text)}
.page{position:relative;width:1200px;height:1425px;transform:scale(.8425);transform-origin:0 0}
.abs{position:absolute}

.brand{left:120px;top:34px;display:flex;align-items:center;gap:12px}
.brand-mark{width:52px;height:52px;border-radius:50%;background:var(--teal)}
.brand-name{font-size:26px;color:#bdbdbd;font-weight:400;line-height:1}

.search{left:835px;top:28px;width:246px;height:26px;background:var(--search);border-radius:2px;font-size:9px;color:#aaa;padding:8px 8px}
.search svg{position:absolute;right:8px;top:8px}

.nav{left:596px;top:66px;display:flex;height:39px}
.nav a{color:var(--text);text-decoration:none;font-size:17px;line-height:39px;padding:0 20px}
.nav a.active{background:var(--teal)}
.nav a:nth-child(2){padding:0 20px 0 13px}
.nav a:nth-child(3){padding:0 18px 0 20px}
.nav a:nth-child(4){padding:0 20px 0 19px}
.nav a:nth-child(5){padding:0 14px 0 21px}
.rule{left:120px;top:105px;width:960px;height:3px;background:var(--teal)}

.hero{left:120px;top:108px;width:960px;height:372px;background:linear-gradient(180deg,#f2d98a 0%,#f6e3a0 35%,#d9a84a 60%,#b9862d 100%)}
.hero-line{left:149px;top:274px;font-size:24px;font-weight:700;color:#fff;opacity:.85}
.dots{left:564px;top:449px;display:flex;gap:5px}
.dots i{width:14px;height:14px;border-radius:50%;background:#fff;display:block}
.dots i:first-child{background:var(--teal)}

.heading{font-size:17px;font-weight:700;text-transform:uppercase;letter-spacing:.2px}

.photo{display:block}
.welcome-photo{left:120px;top:554px;width:630px;height:224px;background:linear-gradient(180deg,#2e6fc4,#4d8fd8)}
.expert-photo{left:769px;top:611px;width:311px;height:166px;background:linear-gradient(90deg,#dfe4e6,#e9d6c6)}
.body-copy{font-size:11.6px;line-height:22px;text-align:justify;color:var(--text)}

.expert-name{left:769px;top:547px;font-size:23px;color:var(--orange)}
.expert-role{left:769px;top:577px;font-size:14px}

.client-photo{left:120px;top:994px;width:114px;height:114px;border-radius:50%;background:linear-gradient(135deg,#e9eef2,#b98a6a)}
.client-name{left:245px;top:1029px;font-size:17px;font-weight:700;color:var(--teal)}
.client-role{left:245px;top:1055px;font-size:14px}

.news-thumb{width:94px;height:79px}
.news-item{font-size:11.6px;line-height:22px;width:210px}
.news-item a{color:var(--teal);text-decoration:none}

.partners{left:0;top:1260px;width:1200px;height:53px;background:var(--band)}
.partners span{position:absolute;top:16px;height:22px;background:var(--badge);border-radius:2px}

.foot-links{left:119px;top:1339px;font-size:14px;display:flex;gap:14px}
.foot-links a{color:var(--text);text-decoration:none}
.copy{left:117px;top:1374px;font-size:14px}
.social{top:1340px;width:36px;height:36px;border-radius:50%;background:#fff}
</style>
</head>
<body>
<div class="page">

  <header>
    <div class="abs brand"><span class="brand-mark"></span><span class="brand-name">Tides Of Bloom</span></div>
    <div class="abs search">Type search
      <svg width="10" height="10" viewBox="0 0 10 10"><circle cx="4" cy="4" r="3" fill="none" stroke="#aaa" stroke-width="1.3"/><line x1="6.2" y1="6.2" x2="9.5" y2="9.5" stroke="#aaa" stroke-width="1.5"/></svg>
    </div>
    <nav class="abs nav">
      <a class="active" href="#">Home</a><a href="#">About Us</a><a href="#">Business</a><a href="#">Individual</a><a href="#">Contact</a>
    </nav>
    <div class="abs rule"></div>
  </header>

  <section>
    <div class="abs hero" role="img" aria-label="Man with raised arms in a golden wheat field at sunrise"></div>
    <p class="abs hero-line">We are catalysts of change in people’s lives.</p>
    <div class="abs dots"><i></i><i></i><i></i><i></i></div>
  </section>

  <section>
    <h2 class="abs heading" style="left:120px;top:511px">Welcome to Tides Of Bloom</h2>
    <div class="abs photo welcome-photo" role="img" aria-label="Woman leaping against a blue sky trailing a green scarf"></div>
    <p class="abs body-copy" style="left:120px;top:797px;width:631px">At vero eos et accusamus et iusto odio dignissimos ducimus qui blanditiis praesentium voluptatum deleniti atque corrupti quos dolores et quas molestias excepturi sint occaecati cupiditate non provident, similique sunt in culpa qui officia deserunt mollitia animi, id est laborum et dolorum fuga. Et harum quidem rerum facilis est et expedita distinctio. Nam libero tempore, cum soluta nobis est eligendi optio cumque nihil impedit quo minus id quod maxime placeat facere possimus, omnis voluptas assumenda est, omnis dolor repellendus. Temporibus autem quibusdam et aut officiis debitis aut rerum</p>
  </section>

  <section>
    <h2 class="abs heading" style="left:770px;top:511px">Expert Practitioner’s</h2>
    <svg class="abs" style="left:1054px;top:511px" width="29" height="18" viewBox="0 0 29 18"><path d="M10 2 3 9l7 7M19 2l7 7-7 7" fill="none" stroke="#fff" stroke-width="2"/></svg>
    <p class="abs expert-name">Lena Harlow</p>
    <p class="abs expert-role">Master Practitioner for 6 years</p>
    <div class="abs photo expert-photo" role="img" aria-label="Smiling practitioner portrait in a bright office"></div>
    <p class="abs body-copy" style="left:767px;top:798px;width:313px">Sed ut perspiciatis unde omnis iste natus error sit voluptatem accusantium doloremque laudantium, totam rem aperiam, eaque ipsa quae ab illo inventore veritatis et quasi architecto beatae vitae dicta sunt explicabo. Nemo enim ipsam voluptatem quia voluptas sit aspernatur aut odit aut fugit</p>
  </section>

  <section>
    <h2 class="abs heading" style="left:120px;top:951px">Client’s Testimonial</h2>
    <svg class="abs" style="left:403px;top:952px" width="29" height="18" viewBox="0 0 29 18"><path d="M10 2 3 9l7 7M19 2l7 7-7 7" fill="none" stroke="#fff" stroke-width="2"/></svg>
    <div class="abs client-photo" role="img" aria-label="Client portrait with laptop"></div>
    <p class="abs client-name">Priya Morel</p>
    <p class="abs client-role">CEO ,Company Name</p>
    <p class="abs body-copy" style="left:135px;top:1126px;width:292px">“.Sed ut perspiciatis unde omnis iste natus error sit voluptatem accusantium doloremque laudantium, totam rem aperiam, eaque ipsa quae ab illo inventore ”</p>
  </section>

  <section>
    <h2 class="abs heading" style="left:451px;top:951px">Business</h2>
    <p class="abs" style="left:451px;top:994px;font-size:14px">Inspiring Business Excellence</p>
    <p class="abs body-copy" style="left:451px;top:1021px;width:301px">Tides Of Bloom have worked with CEO’s &amp; business owners throughout Australia, as catalysts to their outstanding success. We will facilitate &amp; oversee your development of better and more effective ways of increasing performance and improving effectiveness.<br>Imagine your professional life both consistent &amp; predictable. Your effectiveness with others dramatically increased, and having at your fingertips the ability</p>
  </section>

  <section>
    <h2 class="abs heading" style="left:770px;top:951px">Latest News</h2>
    <svg class="abs" style="left:1051px;top:952px" width="29" height="18" viewBox="0 0 29 18"><path d="M10 2 3 9l7 7M19 2l7 7-7 7" fill="none" stroke="#fff" stroke-width="2"/></svg>
    <div class="abs news-thumb" style="left:770px;top:999px;background:linear-gradient(180deg,#cfd3cf,#9aa097)" role="img" aria-label="Man on a ladder with a telescope and hot-air balloon"></div>
    <p class="abs news-item" style="left:872px;top:993px">Sed ut perspiciatis unde omnis iste natus error sit doloremque laudantium, totam rem aperiam, eaque <a href="#">.Read More</a><br>Posted By : TOB,Nov 5th</p>
    <div class="abs news-thumb" style="left:770px;top:1122px;background:linear-gradient(180deg,#6f9fd6,#1d4f8a 60%,#0d2a4d)" role="img" aria-label="City skyline across the water at dusk"></div>
    <p class="abs news-item" style="left:872px;top:1115px">Sed ut perspiciatis unde omnis iste natus error sit doloremque laudantium, totam rem aperiam, eaque <a href="#">Read More</a><br>Posted By : TOB,Nov 5th</p>
  </section>

  <div class="abs partners" aria-label="Featured in">
    <span style="left:131px;width:118px"></span>
    <span style="left:266px;width:75px"></span>
    <span style="left:361px;width:117px"></span>
    <span style="left:505px;width:74px"></span>
    <span style="left:600px;width:97px"></span>
    <span style="left:716px;width:107px"></span>
    <span style="left:854px;width:54px"></span>
    <span style="left:945px;width:94px"></span>
  </div>

  <footer>
    <nav class="abs foot-links">
      <a href="#">Home</a><span>|</span><a href="#">About Us</a><span>|</span><a href="#">Business</a><span>|</span><a href="#">Individual</a><span>|</span><a href="#">Contact</a>
    </nav>
    <p class="abs copy">© 2013 Company Name ,All Rights Reserved</p>
    <span class="abs social" style="left:1002px"></span>
    <span class="abs social" style="left:1045px"></span>
  </footer>

</div>
</body>
</html>
```